Property Investor needs business card

Hi, we need a business card/logo/email footer/letterhead for a small family property investment business (based in Australia), to just give things a bit more of a professional "look".
Saying that, the property manager is in his late 30s, and is a fun, interesting guy so it doesn't have to be too "corporate" and serious.
Going with eg an 8cmx4cm card size could also make it a bit more interesting. Colour-wise - am relaxed.
Also, the property isn't so much "residential" ie houses/apartments, more "commercial" ie factories, office buildings, shops - in case that helps?
Lastly, the business name is "QHT", so you could also try to do something with those letters.
Enjoy!

```html
<!DOCTYPE html>
<html lang="en">
<head>
<meta charset="utf-8">
<title>QHT Property Investments – Business Card</title>
<link href="https://fonts.googleapis.com/css2?family=Didact+Gothic&family=Mulish:wght@700&display=swap" rel="stylesheet">
<style>
  :root {
    --backdrop: #2a2a2a;
    --card: #fbfbfa;
    --accent: #8e2a1c;
    --ink: #3c3c3c;
    --ink-soft: #555555;
    --rule: #3c3c3c;
  }
  html, body {
    margin: 0;
    padding: 0;
    width: 1200px;
    height: 800px;
    overflow: hidden;
    background: var(--backdrop);
  }
  .canvas {
    position: relative;
    width: 1200px;
    height: 800px;
    display: flex;
    align-items: center;
    justify-content: center;
  }
  .business-card {
    position: relative;
    width: 900px;
    height: 500px;
    background: var(--card);
    box-shadow: 0 20px 50px rgba(0,0,0,0.45);
    font-family: "Didact Gothic", sans-serif;
    color: var(--ink);
  }
  .brand {
    position: absolute;
    left: 96px;
    top: 88px;
    display: flex;
    align-items: center;
  }
  .brand-name {
    font-family: "Didact Gothic", sans-serif;
    font-size: 86px;
    letter-spacing: 6px;
    line-height: 1;
    color: var(--accent);
  }
  .brand-rule {
    width: 2px;
    height: 112px;
    background: var(--rule);
    margin: 0 30px 0 40px;
  }
  .brand-tagline {
    font-size: 34px;
    line-height: 1.05;
    color: var(--ink);
  }
  .holder {
    position: absolute;
    left: 0;
    top: 360px;
    width: 400px;
    text-align: right;
  }
  .holder-name {
    font-family: "Mulish", sans-serif;
    font-weight: 700;
    font-size: 27px;
    letter-spacing: 1px;
    color: var(--ink);
    line-height: 1.2;
  }
  .holder-title {
    font-size: 21px;
    color: var(--ink-soft);
    margin-top: 2px;
  }
  .contact-rule {
    position: absolute;
    left: 428px;
    top: 345px;
    width: 2px;
    height: 80px;
    background: var(--rule);
  }
  .contact {
    position: absolute;
    left: 455px;
    top: 340px;
    font-size: 20px;
    line-height: 1.45;
    color: var(--ink-soft);
  }
  .contact-label {
    font-family: "Mulish", sans-serif;
    font-weight: 700;
    color: var(--accent);
  }
</style>
</head>
<body>
  <main class="canvas">
    <section class="business-card" aria-label="QHT Property Investments business card">
      <header class="brand">
        <span class="brand-name">QHT</span>
        <span class="brand-rule"></span>
        <span class="brand-tagline">Property<br>Investments</span>
      </header>

      <div class="holder">
        <div class="holder-name">CASEY MORGAN</div>
        <div class="holder-title">Managing Director</div>
      </div>

      <span class="contact-rule"></span>

      <address class="contact" style="font-style:normal">
        <div class="contact-address">PO Box 4821, Harwood NSQ 2419</div>
        <div class="contact-lines">
          <span class="contact-label">Mob:</span>&nbsp; 0412 555 018
          <span class="contact-label">Email:</span> casey.m@qhtmail.com
        </div>
      </address>
    </section>
  </main>
</body>
</html>
```